Online Dating Ebook Needs an Amazing Cover Design

This is a cover for an online dating ebook that will go online to the Pagewell store and will have a large audience. It is targeted primarily to men and is written from the perspective of a Strategy Consultant

The cover needs to be elegant, seductive and eye catching but not overbearing or cheesy. No pornography, outright nudity, etc. It should draw the eye.

The title is

"Master Web Romance" with the subtitle "A Business Advisor's Handbook"

The author's name would need to be Mark Tellby.

Feel free to send emails asking for feedback on your designs so we can work on many versions

Target Market(s)

Target market is 18-40 year old single males who will be doing online dating

Industry/Entity Type

Dating

Requirements
Must have
• 1)Must be given a .jpg and vector file.

2) Must be 900 pixel Height and 600 pixel width.

3)Need a 300 dpi and 72 dpi version

4) Author's name as Mark Tellby

```html
<!DOCTYPE html>
<html lang="en">
<head>
<meta charset="utf-8">
<title>Master Web Romance — Book Cover</title>
<link rel="stylesheet" href="https://fonts.googleapis.com/css2?family=Special+Elite&family=Nunito+Sans:wght@300;400&display=swap">
<style>
  :root {
    --page-bg: #ffffff;
    --cover-blue-deep: #1466b0;
    --cover-blue-mid: #1f7ec8;
    --cover-blue-glow: #3bb0ea;
    --title-cream: #f6ead0;
    --title-peach: #f3cf94;
    --subtitle-amber: #f2a93b;
    --author-ink: #111418;
    --figure-ink: #0b0d10;
    --shadow-ochre: #d69a2e;
  }

  * { margin: 0; padding: 0; box-sizing: border-box; }

  html, body {
    width: 1200px;
    height: 800px;
    overflow: hidden;
    background: var(--page-bg);
  }

  .stage {
    position: relative;
    width: 1200px;
    height: 800px;
  }

  .book-cover {
    position: absolute;
    left: 389px;
    top: 47px;
    width: 467px;
    height: 700px;
    overflow: hidden;
    background:
      radial-gradient(circle at 66% 19%, var(--cover-blue-glow) 0%, var(--cover-blue-mid) 32%, var(--cover-blue-deep) 78%);
    box-shadow: 0 2px 6px rgba(0, 0, 0, 0.28);
  }

  .cover-subtitle {
    position: absolute;
    top: 22px;
    left: 0;
    width: 100%;
    text-align: center;
    font-family: "Nunito Sans", "Helvetica Neue", Arial, sans-serif;
    font-weight: 300;
    font-size: 25px;
    letter-spacing: 0.4px;
    color: var(--subtitle-amber);
  }

  .cover-title {
    position: absolute;
    left: 8px;
    top: 128px;
    width: 310px;
    font-family: "Special Elite", "Courier New", monospace;
    font-weight: 400;
    color: var(--title-cream);
    line-height: 1;
  }

  .title-line {
    display: block;
    white-space: nowrap;
    font-size: 54px;
    height: 72px;
    line-height: 72px;
  }

  .title-line--second { padding-left: 22px; }
  .title-line--third { padding-left: 40px; }

  .title-line span { display: inline-block; }
  .title-line .cap { font-size: 66px; }
  .title-line .up { transform: translateY(-6px); }
  .title-line .down { transform: translateY(6px); }
  .title-line .warm { color: var(--title-peach); }

  .cover-art {
    position: absolute;
    left: 0;
    top: 0;
    width: 467px;
    height: 700px;
  }

  .cover-author {
    position: absolute;
    left: 0;
    bottom: 22px;
    width: 100%;
    text-align: center;
    font-family: "Nunito Sans", "Helvetica Neue", Arial, sans-serif;
    font-weight: 400;
    color: var(--author-ink);
  }

  .cover-author .by { font-size: 24px; margin-right: 6px; }
  .cover-author .name { font-size: 38px; letter-spacing: 0.5px; }
</style>
</head>
<body>
<main class="stage">
  <section class="book-cover">
    <p class="cover-subtitle">A Business Advisor's Handbook</p>

    <svg class="cover-art" viewBox="0 0 467 700" xmlns="http://www.w3.org/2000/svg">
      <defs>
        <radialGradient id="shadow-fill" cx="50%" cy="50%" r="55%">
          <stop offset="0%" stop-color="var(--shadow-ochre)" stop-opacity="0.95"/>
          <stop offset="100%" stop-color="var(--shadow-ochre)" stop-opacity="0.55"/>
        </radialGradient>
      </defs>
      <g role="img" aria-label="Golden cast shadow of the man stretching across the floor with arms spread wide">
        <ellipse cx="172" cy="556" rx="158" ry="46" fill="url(#shadow-fill)"/>
      </g>
      <g role="img" aria-label="Black silhouette of a man in a suit pointing up toward the title">
        <rect x="338" y="214" width="104" height="406" rx="34" fill="var(--figure-ink)"/>
      </g>
    </svg>

    <h1 class="cover-title" aria-label="Master Web Romance">
      <span class="title-line title-line--first" aria-hidden="true"><span class="cap">M</span><span class="down">a</span><span>s</span><span class="up warm">t</span><span class="down warm">e</span><span class="warm">r</span></span>
      <span class="title-line title-line--second" aria-hidden="true"><span class="cap up">W</span><span class="down warm">e</span><span class="warm">b</span></span>
      <span class="title-line title-line--third" aria-hidden="true"><span class="cap">R</span><span class="down">o</span><span class="up">m</span><span>a</span><span class="down warm">n</span><span class="warm">c</span><span class="up warm">e</span></span>
    </h1>

    <p class="cover-author"><span class="by">by</span><span class="name">Mark Tellby</span></p>
  </section>
</main>
</body>
</html>
```